Poster Design

Hello,

My name is Rowan Pickett and I run a vidora channel called 'CrumbleDiary'. I want a poster made for those who watch my video to purchase and put on their wall at home. The poster will be all text and as you can see, I've attached a few examples of posters which I would like it to be similar to. I use a lot of the colour #ab6f7f so it would be good to incorporate this in somewhere (maybe the background colour).
I would like the poster to say:
"Do More Of What Makes YOU Happy"
I need this poster to be for sale ready for christmas, so Im going to need the designs created as soon as possible. Im sorry for the rush.
Have fun with it and feel free to upload multiple versions of a design as well as a few designs if you like.
I look forward to seeing what you come up with.
Rowan
(Of course I will need to own all rights once the payment has been made)

```html
<!DOCTYPE html>
<html lang="en">
<head>
<meta charset="utf-8">
<title>Do More Of What Makes You Happy – Poster</title>
<link rel="stylesheet" href="https://fonts.googleapis.com/css2?family=Big+Shoulders+Display:wght@600&family=Big+Shoulders+Inline+Display:wght@700&family=Bungee+Inline&family=Playfair+Display:ital,wght@0,400;1,400&display=swap">
<style>
  :root {
    --rose: #ab6f7f;
    --paper: #ffffff;
  }
  html, body {
    margin: 0;
    padding: 0;
    width: 1200px;
    height: 1200px;
    overflow: hidden;
    background: var(--paper);
  }
  .poster {
    display: block;
    width: 1200px;
    height: 1200px;
  }
  .headline-top {
    font-family: "Bungee Inline", "Arial Black", sans-serif;
    font-size: 66px;
    fill: var(--rose);
  }
  .connector {
    font-family: "Playfair Display", Georgia, serif;
    font-style: italic;
    font-size: 42px;
    fill: var(--rose);
  }
  .headline-mid {
    font-family: "Big Shoulders Inline Display", "Arial Narrow", sans-serif;
    font-weight: 700;
    font-size: 146px;
    fill: var(--rose);
  }
  .ribbon-word {
    font-family: "Playfair Display", Georgia, serif;
    font-size: 40px;
    fill: var(--paper);
  }
  .headline-bottom {
    font-family: "Big Shoulders Display", "Arial Narrow", sans-serif;
    font-weight: 600;
    font-size: 178px;
    fill: var(--rose);
  }
  .dot-rule {
    stroke: var(--rose);
    stroke-width: 5;
    stroke-linecap: round;
    stroke-dasharray: 0 9;
    fill: none;
  }
  .thin-rule {
    stroke: var(--rose);
    stroke-width: 2;
    fill: none;
  }
  .ribbon-outline {
    stroke: var(--rose);
    stroke-width: 1.5;
    fill: none;
  }
  .ribbon-fill,
  .accent-dot {
    fill: var(--rose);
  }
</style>
</head>
<body>
<svg class="poster" viewBox="0 0 1200 1200" xmlns="http://www.w3.org/2000/svg" role="img" aria-label="Do more of what makes you happy">
  <rect width="1200" height="1200" fill="var(--paper)"/>

  <!-- Line 1 -->
  <text class="headline-top" x="430" y="372" textLength="342" lengthAdjust="spacingAndGlyphs">DO MORE</text>

  <!-- Line 2 with dotted rules -->
  <g class="connector-row">
    <line class="dot-rule" x1="435" y1="431" x2="500" y2="431"/>
    <text class="connector" x="601" y="440" text-anchor="middle">of what</text>
    <line class="dot-rule" x1="696" y1="431" x2="768" y2="431"/>
  </g>

  <!-- Line 3 -->
  <text class="headline-mid" x="432" y="578" textLength="340" lengthAdjust="spacingAndGlyphs">MAKES</text>

  <!-- Ribbon -->
  <g class="ribbon">
    <line class="thin-rule" x1="432" y1="628" x2="472" y2="628"/>
    <line class="thin-rule" x1="432" y1="638" x2="472" y2="638"/>
    <line class="thin-rule" x1="728" y1="628" x2="770" y2="628"/>
    <line class="thin-rule" x1="728" y1="638" x2="770" y2="638"/>
    <polygon class="ribbon-outline" points="455,601 747,601 726,633 747,665 455,665 476,633"/>
    <polygon class="ribbon-fill" points="467,608 735,608 716,633 735,658 467,658 486,633"/>
    <text class="ribbon-word" x="601" y="648" text-anchor="middle">YOU</text>
  </g>

  <!-- Line 4 -->
  <g class="bottom-row">
    <circle class="accent-dot" cx="437" cy="742" r="7"/>
    <text class="headline-bottom" x="470" y="815" textLength="260" lengthAdjust="spacingAndGlyphs">HAPPY</text>
    <circle class="accent-dot" cx="762" cy="742" r="7"/>
  </g>
</svg>
</body>
</html>
```